LuMarking-Tagvelory Partial Redesign - Web App

Are you able to apply your creativity to an existing layout? I’m convinced that even just a few touches can make a big difference to add personality and professionalism to a website design, and I’m looking for someone able to use existing ideas and bring them to the next level while keeping inside some given constraints.
The actual job is to improve an existing design concept and to apply it creatively to a landing page, a simple home page, and an older web app (single page website).
To help you start with a clear picture of the current situation and of my requirements, I created a detailed brief with screenshots, live examples, and complete instructions. You can find it attached to this job.
My tastes are inclined towards clean and simple designs. For this project I'm not looking for dazzling novelty, but for very solid craftsmanship. Are the right man - or woman - for the job?
Updates
I wanted to thank everybody who participated in this project. I made a choice, but also other designs were interesting. Hope to work with you another time.
Target Market(s)
Our main target is social media marketers and startuppers
Look and feel
Each slider illustrates characteristics of the customer's brand and the style your logo design should communicate.

```html
<!DOCTYPE html>
<html lang="en">
<head>
<meta charset="utf-8">
<title>LuMarking — Social media analytics</title>
<link href="https://fonts.googleapis.com/css2?family=Open+Sans:wght@300;400;600;700&family=Arimo:wght@400;700&display=swap" rel="stylesheet">
<style>
:root{
  --page:#e7e7e7;
  --ink:#1f1f1f;
  --text:#3a3a3a;
  --muted:#8a8a8a;
  --heading:#2c5d8f;
  --accent:#4fb3e6;
  --pill-dark:#1d1d1d;
  --pill-mid:#3f3f3f;
  --pill-grey:#6a6a6a;
  --panel:#f5f5f5;
  --line:#dadada;
  --footer:#232323;
  --hero-a:#7fb6d4;
  --hero-b:#2a5f8f;
  --hero-c:#1c2533;
}
*{margin:0;padding:0;box-sizing:border-box}
html,body{width:1200px;height:1110px;overflow:hidden}
body{position:relative;background:linear-gradient(#e9e9e9,#f6f6f6 600px,#fafafa);font-family:"Arimo",Arial,sans-serif;color:var(--text)}
.abs{position:absolute}

.site-header{position:absolute;left:0;top:0;width:1200px;height:101px;background:linear-gradient(#ffffff,#f1f1f1);border-bottom:1px solid #cfcfcf;box-shadow:0 1px 3px rgba(0,0,0,.12)}
.brand{position:absolute;left:132px;top:30px;display:flex;align-items:center;gap:12px;font-family:"Open Sans",sans-serif;font-weight:700;font-size:29px;color:var(--ink);letter-spacing:-.5px}
.brand-dot{width:34px;height:34px;border-radius:50%;background:var(--ink)}

.pill{position:absolute;top:33px;height:33px;border-radius:17px;background:linear-gradient(var(--pill-mid),var(--pill-dark));color:#fff;font-family:"Open Sans",sans-serif;font-weight:700;font-size:12.5px;display:flex;align-items:center;justify-content:center;gap:8px;box-shadow:0 2px 3px rgba(0,0,0,.35),inset 0 1px 0 rgba(255,255,255,.2)}
.pill.light{background:linear-gradient(#8a8a8a,#5d5d5d)}
.caret{width:0;height:0;border-left:3px solid transparent;border-right:3px solid transparent;border-top:4px solid #bbb}
.nav-rule{position:absolute;top:49px;height:1px;background:#d4d4d4}

.hero{position:absolute;left:120px;top:116px;width:960px;height:436px;overflow:hidden;box-shadow:0 1px 3px rgba(0,0,0,.3)}
.hero-photo{position:absolute;inset:0;background:radial-gradient(circle at 770px 300px,rgba(230,240,250,.55),transparent 180px),linear-gradient(90deg,var(--hero-a) 0%,#5a95bf 30%,var(--hero-b) 55%,var(--hero-c) 75%,#2b3442 100%)}
.hero-track{position:absolute;right:0;top:0;width:10px;height:436px;background:#e6e6e6}
.hero-thumb{position:absolute;right:2px;top:0;width:8px;height:145px;background:#1f5a96}
.hero-kicker{position:absolute;left:38px;top:56px;font-family:"Open Sans",sans-serif;font-weight:600;font-size:15px;color:#fff;letter-spacing:.4px}
.hero-title{position:absolute;left:36px;top:82px;font-family:"Open Sans",sans-serif;font-weight:300;font-size:44px;line-height:49px;color:#fff;text-shadow:0 1px 2px rgba(0,0,0,.3)}
.hero-rule{position:absolute;left:38px;top:213px;width:112px;height:1px;background:rgba(255,255,255,.35)}
.hero-copy{position:absolute;left:38px;top:244px;width:380px;font-family:"Open Sans",sans-serif;font-size:12.3px;line-height:18px;color:#fff}
.btn{position:absolute;height:34px;border-radius:17px;color:#fff;font-family:"Open Sans",sans-serif;font-weight:700;font-size:12.5px;display:flex;align-items:center;padding-left:19px;box-shadow:0 2px 3px rgba(0,0,0,.35),inset 0 1px 0 rgba(255,255,255,.2)}
.btn::after{content:"›";position:absolute;right:18px;font-weight:400;color:#aaa}
.btn-dark{background:linear-gradient(#3a3a3a,#121212)}
.btn-grey{background:linear-gradient(#8c8c8c,#555)}

.panel{position:absolute;background:linear-gradient(#f2f2f2,#fcfcfc);border:1px solid var(--line)}
.panel h2{position:absolute;font-family:"Open Sans",sans-serif;font-weight:400;font-size:30px;color:var(--heading)}
.lead{position:absolute;left:10px;top:72px;width:600px;font-weight:700;font-size:12.5px;line-height:18px;color:var(--ink)}
.body-copy{position:absolute;left:10px;top:126px;width:605px;font-size:12.3px;line-height:18px}
.sub{position:absolute;left:10px;top:204px;font-weight:700;font-size:12.5px;color:var(--ink)}
.points{position:absolute;left:26px;top:246px;list-style:none;font-size:12.3px}
.points li{height:24px;padding-left:20px;position:relative}
.points li::before{content:"→";position:absolute;left:0;color:#999;font-size:11px}

.feature{position:absolute;left:28px;width:240px}
.feature svg{position:absolute;left:0;top:0}
.feature h3{position:absolute;left:56px;top:0;font-size:12.5px;font-weight:700;color:var(--ink);white-space:nowrap}
.feature p{position:absolute;left:56px;top:18px;width:200px;font-size:12.3px;line-height:18px}

.help{position:absolute;left:770px;top:913px;width:310px;height:82px;background:linear-gradient(#2f6fa7,#1a4f86);box-shadow:0 1px 3px rgba(0,0,0,.3)}
.help strong{position:absolute;left:19px;top:25px;font-family:"Open Sans",sans-serif;font-weight:700;font-size:23px;color:#fff}
.help-rule{position:absolute;left:167px;top:0;width:1px;height:82px;background:rgba(255,255,255,.18)}
.help p{position:absolute;left:189px;top:20px;width:110px;font-size:10.5px;line-height:14px;color:#cfe2f3}

.site-footer{position:absolute;left:0;top:1009px;width:1200px;height:101px;background:var(--footer);color:#cfcfcf;font-size:11px}
.foot-brand{position:absolute;left:133px;top:17px;font-family:"Open Sans",sans-serif;font-weight:700;font-size:18px;color:#fff}
.foot-address{position:absolute;left:133px;top:50px;line-height:18px;color:#d6d6d6}
.foot-rule{position:absolute;left:271px;top:2px;width:1px;height:68px;background:#3a3a3a}
.foot-links{position:absolute;left:310px;top:24px;display:flex;color:#fff}
.foot-links a{color:#fff;text-decoration:none}
.foot-links a+a{margin-left:10px;padding-left:10px;border-left:1px solid #444}
.copyright{position:absolute;left:310px;top:51px;color:#7d7d7d}
.to-top{position:absolute;right:120px;top:24px;color:#7d7d7d}
</style>
</head>
<body>

<header class="site-header">
  <div class="brand"><span class="brand-dot"></span>LuMarking</div>
  <nav>
    <a class="pill" style="left:450px;width:48px" aria-label="Home">
      <svg width="13" height="12" viewBox="0 0 13 12"><path d="M6.5 0 0 6h2v6h3.5V8h2v4H11V6h2z" fill="#fff"/></svg>
    </a>
    <a class="pill" style="left:509px;width:105px">Products <span class="caret"></span></a>
    <span class="nav-rule" style="left:625px;width:110px"></span>
    <a class="pill" style="left:745px;width:63px">Blog</a>
    <a class="pill" style="left:819px;width:72px">About</a>
    <span class="nav-rule" style="left:902px;width:20px"></span>
    <a class="pill light" style="left:932px;width:63px">Help</a>
    <a class="pill light" style="left:1006px;width:63px" aria-label="Account">
      <svg width="12" height="12" viewBox="0 0 12 12"><circle cx="6" cy="3.5" r="3" fill="#fff"/><path d="M0 12c0-4 3-5.5 6-5.5s6 1.5 6 5.5z" fill="#fff"/></svg>
      <span class="caret"></span>
    </a>
  </nav>
</header>

<section class="hero">
  <div class="hero-photo" role="img" aria-label="Photo of a businessman in a suit touching a glowing globe surrounded by social media icons"></div>
  <div class="hero-track"><div class="hero-thumb"></div></div>
  <p class="hero-kicker">LOREM IPSUM DOLOR SIT AMENT</p>
  <h1 class="hero-title">Nulla pretium tortor<br>a odio sagittis</h1>
  <span class="hero-rule"></span>
  <p class="hero-copy">Lorem ipsum dolor sit amet, consectetur adipiscing elit. Vestibulum vestibulum mauris arcu. Nunc nisl elit, imperdiet non laoreet et, cursus eget justo. Proin congue facilisis fringilla. Etiam iaculis vulputate a rutrum.</p>
  <a class="btn btn-dark" style="left:36px;top:342px;width:160px">View more details</a>
</section>

<section class="panel" style="left:120px;top:567px;width:630px;height:427px">
  <h2 style="left:10px;top:16px">About LuMarking</h2>
  <p class="lead">LuMarking Ltd. is a marketing savvy social media analytics company. Our mission is to help social media marketers reach their branding goals and validate their approach with their PulseSocial campaigns.</p>
  <p class="body-copy">Mauris malesuada purus sed orci ullamcorper tempor. Nulla sit amet eros nisi. Pellentesque ornare sagittis diam, et condimentum libero molestie eget. Mauris a purus velit, non congue nunc. In elementum felis et nunc cursus sagittis. Praesent pharetra tincidunt justo, sed egestas risus volutpat vel.</p>
  <p class="sub">Praesent elit libero, imperdiet eu venenatis et, viverra et lorem:</p>
  <ul class="points">
    <li>Lorem ipsum dolor sit amet, consectetur adipiscing elit.</li>
    <li>Nulla pretium tortor a odio sagittis eget lacinia erat ultricies.</li>
    <li>Aenean venenatis lacinia erat, vitae gravida risus tempus et.</li>
    <li>Curabitur tempor metus quis nisi varius et sodales nisi dapibus.</li>
  </ul>
  <a class="btn btn-grey" style="left:10px;top:363px;width:116px">Read more</a>
</section>

<section class="panel" style="left:770px;top:567px;width:310px;height:331px">
  <h2 style="left:19px;top:16px">Why LuMarking?</h2>
  <div class="feature" style="top:84px">
    <svg width="32" height="32" viewBox="0 0 32 32" fill="none" stroke="var(--accent)" stroke-width="1.5"><circle cx="16" cy="16" r="14"/><ellipse cx="16" cy="16" rx="6" ry="14"/><path d="M2 16h28M4.5 9h23M4.5 23h23"/></svg>
    <h3>Mauris malesuada</h3>
    <p>Purus sed orci ullamcorper tempor. Nulla sit amet eros nisi.</p>
  </div>
  <div class="feature" style="top:156px">
    <svg width="32" height="34" viewBox="0 0 32 34" fill="none" stroke="var(--accent)" stroke-width="1.5"><path d="M10 14V9a6 6 0 0 1 12 0v5"/><rect x="7" y="14" width="18" height="16" rx="1"/><path d="M7 21h18"/></svg>
    <h3>Pellentesque ornare</h3>
    <p>Sagittis diam, et condimentum libero molestie eget. Mauris a purus velit, non congue nunc.</p>
  </div>
  <div class="feature" style="top:246px">
    <svg width="32" height="34" viewBox="0 0 32 34" fill="none" stroke="var(--accent)" stroke-width="1.5"><path d="M16 2 3 6v10c0 8 6 13 13 16 7-3 13-8 13-16V6z"/><path d="M16 2v30"/></svg>
    <h3>In elementum felis et nunc</h3>
    <p>Cursus sagittis. Praesent pharetra tincidunt justo, sed egestas risus volutpat vel.</p>
  </div>
</section>

<aside class="help">
  <strong>Need help?</strong>
  <span class="help-rule"></span>
  <p>Curabitur tempor metus quis nisi variu et sodales nisi ›</p>
</aside>

<footer class="site-footer">
  <div class="foot-brand">LuMarking</div>
  <address class="foot-address" style="font-style:normal">48 Fenwick Lane<br>N7 4QT London, UK</address>
  <span class="foot-rule"></span>
  <nav class="foot-links"><a href="#">Privacy Policy</a><a href="#">Terms Of Service</a></nav>
  <p class="copyright">Copyright © 2011-2012 LuMarking Ltd. All Rights Reserved.</p>
  <a class="to-top">Back to top &nbsp;˄</a>
</footer>

</body>
</html>
```